RP Window Cleaning Flyer Design

USE LOGO ATTACHED. Not sure if Images included will look good or not, but maybe try and see.Wording for the leaflet along the lines of:We are a Professional & Personal Family run business offering a Regular & Reliable Service.Though we primarily do Window Cleaning, we also specialise in other services such as Gutter Clearing, Solar Panel Cleaning & Facia/Soffit Cleaning.For these services we utilise the latest equipment and technology including:- Pure Hot Water Cleaning System with telescopic poles to reach up to 40ft- DrainPull – an industrial strength gutter vacuum to suck our the dirt from gutters through specially designed poles(HIGHLIGHTED LINE) - We Clean the Windows for Houses in this Area, Would you like a Quote??For a FREE Quote Please Contact Us:Office: 01892 512677Mobile: 07730 613555info@RPwindowcleaning.co.ukwww.RPwindowcleaning.co.uk - **INSTANT QUOTE** - Use 'Contact Us' Form on our web site & add images of your property, we will then provide a quote with-in 48 Hours.

Target Market(s)

Domestic Customers

Industry/Entity Type

Window Cleaning

Font styles to use
Sans Serif

Colors
3176b5
85acd3
d0dfed
eaf1f7
ffffff
33a6d7
85cae6
cee9f5
ecf7fb

Requirements
Nice to have
• We are having a web site designed at the moment. Please see http://bvkpreviewsite.examplehost.com/rpwindowcleaning/contact-us/ and search the various pages to see our style and wording.

```html
<!DOCTYPE html>
<html lang="en">
<head>
<meta charset="utf-8">
<title>RP Window Cleaning Flyer</title>
<link href="https://fonts.googleapis.com/css2?family=Montserrat:wght@400;500;600;700;800&family=Roboto+Condensed:wght@400;700&display=swap" rel="stylesheet">
<style>
  :root {
    --ink: #15191f;
    --navy-dark: #1b1f2a;
    --brand-blue: #1f5fae;
    --band-blue: #1d5bb0;
    --sky: #c6e5f0;
    --sky-pale: #eaf5fa;
    --white: #ffffff;
    --red: #e8232a;
    --page: #f4f1ec;
  }
  * { margin: 0; padding: 0; box-sizing: border-box; }
  html, body { width: 1200px; height: 1200px; overflow: hidden; background: var(--page); }
  body { font-family: "Montserrat", Arial, sans-serif; color: var(--ink); }

  .flyer {
    position: absolute; left: 40px; top: 204px;
    width: 1120px; height: 792px; overflow: hidden;
    background: linear-gradient(180deg, var(--sky) 0%, #d9eef6 45%, var(--white) 80%);
    box-shadow: 0 4px 14px rgba(0,0,0,.18);
  }
  .contact-panel {
    position: absolute; left: 679px; top: 0; width: 415px; height: 792px;
    background: linear-gradient(180deg, #f6fafc 0%, var(--white) 30%);
  }
  .edge-strip {
    position: absolute; left: 1094px; top: 0; width: 26px; height: 440px;
    background: var(--sky);
  }
  .blue-band { position: absolute; left: 0; top: 596px; width: 700px; height: 52px; background: var(--band-blue); }
  .dark-base { position: absolute; left: 0; top: 648px; width: 1120px; height: 144px; background: var(--navy-dark); }

  .headline {
    position: absolute; left: 29px; top: 48px;
    font-weight: 800; font-size: 45px; line-height: 46px; letter-spacing: -0.5px;
    text-transform: uppercase; color: var(--ink); white-space: nowrap;
  }
  .headline .accent { color: var(--brand-blue); }

  .intro, .equipment-lead {
    position: absolute; left: 29px;
    font-size: 17px; line-height: 24.5px; font-weight: 400;
  }
  .intro { top: 174px; width: 630px; }
  .equipment-lead { top: 358px; width: 600px; }

  .services { position: absolute; left: 189px; top: 256px; list-style: none; }
  .services li {
    display: flex; align-items: center; gap: 12px;
    height: 30.5px; font-size: 19px; font-weight: 600;
  }
  .services svg { width: 22px; height: 22px; }

  .equipment { position: absolute; left: 29px; top: 418px; width: 620px; list-style: none; }
  .equipment li {
    position: relative; padding-left: 18px; margin-bottom: 6px;
    font-size: 17px; line-height: 24.5px; white-space: nowrap;
  }
  .equipment li::before {
    content: ""; position: absolute; left: 2px; top: 10px;
    width: 6px; height: 6px; border-radius: 50%; background: var(--brand-blue);
  }
  .equipment strong { font-weight: 700; }

  .gallery-photo {
    position: absolute; top: 545px; height: 141px;
    border: 3px solid var(--white);
  }
  .photo-brush { left: 30px; width: 189px; background: linear-gradient(160deg, #c9d6df 0%, #8b6a55 45%, #3d3a36 70%, #7a8a5a 100%); }
  .photo-house { left: 231px; width: 188px; background: linear-gradient(180deg, #3e3c3a 0%, #3e3c3a 18%, #9b5a3d 30%, #8a4e36 80%, #5d5a4a 100%); }
  .photo-solar { left: 431px; width: 188px; background: linear-gradient(180deg, #7fb0de 0%, #a8c9ea 25%, #3b4e74 35%, #2a3555 75%, #1d2335 100%); }

  .instant-badge {
    position: absolute; left: 30px; top: 711px; width: 112px; height: 81px;
    background: var(--red); border-radius: 8px 8px 0 0;
    color: var(--white); font-weight: 700; font-size: 20px; line-height: 24px;
    text-align: center; padding-top: 10px;
  }
  .instant-text {
    position: absolute; left: 163px; top: 727px; width: 480px;
    font-family: "Roboto Condensed", Arial, sans-serif;
    font-size: 15.5px; line-height: 22px; color: var(--white);
  }
  .instant-text strong { font-weight: 700; }

  .van-photo {
    position: absolute; left: 650px; top: 430px; width: 470px; height: 362px;
    background:
      linear-gradient(180deg, var(--white) 0%, rgba(255,255,255,0) 30%),
      linear-gradient(90deg, rgba(255,255,255,0.9) 0%, rgba(255,255,255,0) 20%),
      linear-gradient(160deg, #d4d9dd 0%, #a7aeb4 35%, #6e757c 60%, #3a3f45 85%, #55575a 100%);
  }

  .brand {
    position: absolute; left: 699px; top: 31px; width: 377px; height: 123px;
    display: flex; align-items: center; gap: 16px;
  }
  .brand-dot { width: 118px; height: 118px; border-radius: 50%; background: var(--brand-blue); flex: none; }
  .brand-name { font-weight: 700; font-size: 30px; line-height: 34px; color: var(--ink); }

  .quote-heading {
    position: absolute; left: 699px; top: 176px; width: 377px; height: 64px;
    border-top: 2px solid var(--brand-blue); border-bottom: 2px solid var(--brand-blue);
    padding-top: 7px; white-space: nowrap;
  }
  .quote-heading h2 { font-size: 21px; line-height: 26px; font-weight: 800; letter-spacing: -0.5px; }
  .quote-heading p { font-size: 15.5px; line-height: 20px; font-weight: 600; text-transform: uppercase; letter-spacing: -0.2px; }
  .quote-heading .accent { color: var(--brand-blue); }

  .contact-list { position: absolute; left: 738px; top: 256px; list-style: none; white-space: nowrap; }
  .contact-list li { height: 30.5px; font-size: 19px; font-weight: 500; display: flex; align-items: center; }
  .contact-list .label { width: 96px; }
  .contact-list .web { font-size: 16px; }

  .social-handle {
    position: absolute; left: 738px; top: 390px;
    display: flex; align-items: center; gap: 10px;
    font-size: 18px; font-weight: 500; color: var(--brand-blue);
  }
  .social-handle .square { width: 24px; height: 24px; background: var(--ink); border-radius: 4px; }
</style>
</head>
<body>
  <div class="flyer">
    <div class="contact-panel"></div>
    <div class="edge-strip"></div>
    <div class="blue-band"></div>
    <div class="dark-base"></div>

    <h1 class="headline">We <span class="accent">clean</span> the windows<br>for houses in this area</h1>

    <p class="intro">We are a Professional &amp; Personal Family run business offering a<br>Regular &amp; Reliable Service. Though we primarily do Window Cleaning,<br>we also specialise in other services such as</p>

    <ul class="services">
      <li><svg viewBox="0 0 24 24"><circle cx="12" cy="12" r="10" fill="none" stroke="#1f5fae" stroke-width="2.4"/><path d="M7 12.5l3.5 3.5L20 5" fill="none" stroke="#1f5fae" stroke-width="2.8" stroke-linecap="round"/></svg>Gutter Clearing,</li>
      <li><svg viewBox="0 0 24 24"><circle cx="12" cy="12" r="10" fill="none" stroke="#1f5fae" stroke-width="2.4"/><path d="M7 12.5l3.5 3.5L20 5" fill="none" stroke="#1f5fae" stroke-width="2.8" stroke-linecap="round"/></svg>Solar Panel Cleaning</li>
      <li><svg viewBox="0 0 24 24"><circle cx="12" cy="12" r="10" fill="none" stroke="#1f5fae" stroke-width="2.4"/><path d="M7 12.5l3.5 3.5L20 5" fill="none" stroke="#1f5fae" stroke-width="2.8" stroke-linecap="round"/></svg>Facia/Soffit Cleaning</li>
    </ul>

    <p class="equipment-lead">For these services we utilise the latest equipment and technology including:</p>

    <ul class="equipment">
      <li><strong>Pure Hot Water</strong> Cleaning System with telescopic poles<br>to reach up to 40ft</li>
      <li><strong>DrainPull</strong> – an industrial strength gutter vacuum to suck our<br>the dirt from gutters through specially designed poles</li>
    </ul>

    <div class="gallery-photo photo-brush" role="img" aria-label="Photo of a cleaning brush on a pole at a house window"></div>
    <div class="gallery-photo photo-house" role="img" aria-label="Photo of a brick house being cleaned with a telescopic pole"></div>
    <div class="gallery-photo photo-solar" role="img" aria-label="Photo of rooftop solar panels under blue sky"></div>

    <div class="van-photo" role="img" aria-label="Photo of the company van with ladders and open rear doors"></div>

    <div class="instant-badge">INSTANT<br>QUOTE</div>
    <p class="instant-text">Use <strong>'Contact Us'</strong> Form on our web site &amp; add images of your property,<br>we will then provide a quote with-in 48 Hours.</p>

    <div class="brand">
      <div class="brand-dot"></div>
      <div class="brand-name">RP Window<br>Cleaning</div>
    </div>

    <div class="quote-heading">
      <h2>WOULD YOU LIKE A QUOTE??</h2>
      <p>For a <span class="accent">free quote</span> please contact us</p>
    </div>

    <ul class="contact-list">
      <li><span class="label">Office:</span>01734 908214</li>
      <li><span class="label">Mobile:</span>07581 246930</li>
      <li class="web">info@RPwindowcleaning.example.co.uk</li>
      <li class="web">www.RPwindowcleaning.example.co.uk</li>
    </ul>

    <div class="social-handle"><span class="square"></span>RPwindowcleaning</div>
  </div>
</body>
</html>
```